Maple Sprout Menu (Vegetarian Restaurant Concept)

Maple Sprout is a new concept fast casual restaurant
renders are attached so you can see the style of restaurant
Maple Sproutt is a vibrant and modern Vegetarian fast casual restaurant concept that mixes fresh food, energy, great décor, and a comfortable, welcoming atmosphere to provide a memorable and all Vegetarian dining experience.
Our Mission is to be top of mind when consumers think Vegetarian food!
Target Market(s)
the menu is vegetarian and appeals to a broad demographic in USA
Colors
Designer to choose colors to be used in the design.
Requirements
Must have
- well colored and well laid out menu - should not be cartoonish
Nice to have
- For Phots please use the shots in this file:
- https://www.filecrate-example.com/sh/qwx7tr2bnm4kdle/BBBdK_pQrLmNZTHO5E_XYZ_Kb?dl=0
- note these are untouched and you are free to change as needed
Should not have
- Should not be cartoonish - nor kives, forks etc in the design

```html
<!DOCTYPE html>
<html lang="en">
<head>
<meta charset="utf-8">
<title>Maple Sproutt — Menu</title>
<link rel="stylesheet" href="https://fonts.googleapis.com/css2?family=Josefin+Sans:wght@300;400;600;700&family=Quicksand:wght@400;500&display=swap">
<style>
  :root {
    --paper: #ffffff;
    --section-green: #5b8a22;
    --item-green: #1f3814;
    --desc-grey: #6d7760;
    --price-grey: #4a4a4a;
    --rule-grey: #a9aea3;
    --frame-green: #9dbb7a;
    --divider-green: #9fd08a;
  }
  * { margin: 0; padding: 0; box-sizing: border-box; }
  html, body { width: 1200px; height: 927px; overflow: hidden; background: var(--paper); }
  .menu { position: relative; width: 1200px; height: 927px; background: var(--paper); }

  .column-divider {
    position: absolute; top: 12px; bottom: 12px; width: 0;
    border-left: 1px dashed var(--divider-green);
  }

  .section-title {
    position: absolute; display: flex; align-items: center; justify-content: center;
    border: 1px dashed var(--frame-green);
    font-family: "Josefin Sans", sans-serif; font-weight: 400;
    color: var(--section-green); font-size: 20px; letter-spacing: 4px;
    text-align: center; line-height: 27px; padding-top: 3px;
  }

  .item { position: absolute; text-align: center; white-space: nowrap; }
  .col-left  { left: 30px;  width: 378px; }
  .col-mid   { left: 412px; width: 376px; }
  .col-right { left: 790px; width: 376px; }

  .item-name {
    font-family: "Josefin Sans", sans-serif; font-weight: 600;
    font-size: 14px; letter-spacing: 3px; line-height: 21px;
    color: var(--item-green); text-transform: uppercase; padding-top: 2px;
  }
  .item-desc {
    margin-top: 7px;
    font-family: "Quicksand", sans-serif; font-weight: 400;
    font-size: 13px; letter-spacing: 0.8px; line-height: 21px;
    color: var(--desc-grey);
  }
  .item-price {
    margin-top: 3px;
    font-family: "Quicksand", sans-serif; font-weight: 500;
    font-size: 13px; line-height: 16px; color: var(--price-grey);
  }
  .item-name + .item-price { margin-top: 10px; }

  .rule { position: absolute; height: 0; border-top: 1.5px dotted var(--rule-grey); }

  .brand-rule {
    position: absolute; left: 55px; width: 327px; top: 736px; height: 0;
    border-top: 3px dotted var(--section-green);
  }
  .tagline {
    position: absolute; left: 30px; width: 378px; top: 763px; text-align: center;
    font-family: "Josefin Sans", sans-serif; font-weight: 400;
    font-size: 17px; letter-spacing: 2px; line-height: 35px; color: var(--section-green);
  }
  .website {
    position: absolute; left: 136px; width: 167px; top: 866px; text-align: center;
    font-family: "Quicksand", sans-serif; font-weight: 500;
    font-size: 11px; letter-spacing: 2.2px; line-height: 17px;
    color: var(--section-green);
    border-bottom: 1px solid var(--section-green); padding-bottom: 2px;
  }

  .ornament {
    position: absolute; top: 358px; width: 74px; height: 136px;
    background: linear-gradient(180deg, #eef5e4, #dcead0 50%, #eef5e4);
    border-radius: 4px;
  }
  .brand-mark { position: absolute; left: 540px; top: 372px; width: 120px; text-align: center; }
  .brand-dot {
    width: 46px; height: 46px; margin: 0 auto 14px; border-radius: 50%;
    background: var(--section-green);
  }
  .brand-name {
    font-family: "Josefin Sans", sans-serif; font-weight: 600;
    font-size: 17px; letter-spacing: 1px; line-height: 22px; color: var(--item-green);
    white-space: nowrap; margin-left: -20px; margin-right: -20px;
  }
</style>
</head>
<body>
<main class="menu">
  <div class="column-divider" style="left:409px"></div>
  <div class="column-divider" style="left:789px"></div>

  <!-- Salads -->
  <h2 class="section-title" style="left:163px;top:30px;width:113px;height:47px">SALADS</h2>

  <div class="item col-left" style="top:96px">
    <h3 class="item-name">Brussel Sprout Caesar</h3>
    <p class="item-desc">little gem romaine, toasted torn bread,<br>parmigiano reggiano</p>
    <p class="item-price">5</p>
  </div>
  <div class="rule" style="left:30px;width:378px;top:195px"></div>

  <div class="item col-left" style="top:205px">
    <h3 class="item-name">Heirloom Beet Salad</h3>
    <p class="item-desc">shaved chioggia beet, roasted golden beet, red<br>quinoa, little gem, arugula, lemon vinaigrette</p>
    <p class="item-price">5</p>
  </div>
  <div class="rule" style="left:30px;width:378px;top:304px"></div>

  <div class="item col-left" style="top:315px">
    <h3 class="item-name">Zesty Black Bean &amp; Corn Salad in<br>Lettuce Cups</h3>
    <p class="item-desc">black beans, avocado &amp; roasted corn topped with<br>feta crumbles in butter lettuce</p>
    <p class="item-price">5</p>
  </div>
  <div class="rule" style="left:30px;width:378px;top:434px"></div>

  <div class="item col-left" style="top:444px">
    <h3 class="item-name">Green, Red and White</h3>
    <p class="item-desc">spring leaves, cherry tomatoes, avocado, roasted<br>almond &amp; goat cheese</p>
    <p class="item-price">5</p>
  </div>

  <!-- Soup -->
  <h2 class="section-title" style="left:163px;top:568px;width:113px;height:47px">SOUP</h2>
  <div class="item col-left" style="top:636px">
    <h3 class="item-name">Black Bean Chowder</h3>
    <p class="item-price">5</p>
  </div>

  <div class="brand-rule"></div>
  <p class="tagline">‘revolutionizing the vegetarian<br>food experience’</p>
  <p class="website">www.maplesproutt-example.com</p>

  <!-- Toasts -->
  <h2 class="section-title" style="left:543px;top:29px;width:113px;height:48px">TOASTS</h2>

  <div class="item col-mid" style="top:95px">
    <h3 class="item-name">Everything Avocado Toast</h3>
    <p class="item-desc">avocado on whole grain toast with our signature<br>spice blend</p>
    <p class="item-price">5</p>
  </div>
  <div class="rule" style="left:412px;width:376px;top:197px"></div>

  <div class="item col-mid" style="top:207px">
    <h3 class="item-name">Tomato &amp; Beet Bruschetta</h3>
    <p class="item-price">5</p>
  </div>
  <div class="rule" style="left:412px;width:376px;top:268px"></div>

  <div class="item col-mid" style="top:277px">
    <h3 class="item-name">Vegetable Melt on Garlic Toast</h3>
    <p class="item-price">5</p>
  </div>

  <div class="ornament" style="left:451px" role="img" aria-label="Decorative green dotted stripes"></div>
  <div class="ornament" style="left:675px" role="img" aria-label="Decorative green dotted stripes"></div>
  <div class="brand-mark">
    <div class="brand-dot"></div>
    <p class="brand-name">Maple Sproutt</p>
  </div>

  <!-- Bowls -->
  <h2 class="section-title" style="left:544px;top:531px;width:113px;height:48px">BOWLS</h2>

  <div class="item col-mid" style="top:601px">
    <h3 class="item-name">Roasted Vegetable, &amp; Spinach Bowl</h3>
    <p class="item-price">5</p>
  </div>
  <div class="rule" style="left:412px;width:376px;top:661px"></div>

  <div class="item col-mid" style="top:671px">
    <h3 class="item-name">Sugar Snap Pea &amp; Carrot Soba<br>Noodles</h3>
    <p class="item-price">5</p>
  </div>
  <div class="rule" style="left:412px;width:376px;top:751px"></div>

  <div class="item col-mid" style="top:761px">
    <h3 class="item-name">Whole Grain &amp; Vegetable Buddha<br>Bowl</h3>
    <p class="item-price">5</p>
  </div>
  <div class="rule" style="left:412px;width:376px;top:842px"></div>

  <div class="item col-mid" style="top:852px">
    <h3 class="item-name">Orange &amp; Pistachio Quinoa</h3>
    <p class="item-price">5</p>
  </div>

  <!-- Burgers, wraps & sandwiches -->
  <h2 class="section-title" style="left:845px;top:26px;width:269px;height:69px">BURGERS, WRAPS &amp;<br>SANDWICHES</h2>

  <div class="item col-right" style="top:115px">
    <h3 class="item-name">Sweet Potato, Black Bean Veggie<br>Burgers with Cabbage-Pepita Slaw</h3>
    <p class="item-price">5</p>
  </div>
  <div class="rule" style="left:790px;width:376px;top:196px"></div>

  <div class="item col-right" style="top:206px">
    <h3 class="item-name">Roasted Veggie, Arugula &amp; Hummus<br>Wraps</h3>
    <p class="item-price">5</p>
  </div>
  <div class="rule" style="left:790px;width:376px;top:287px"></div>

  <div class="item col-right" style="top:297px">
    <h3 class="item-name">Garden Burger</h3>
    <p class="item-price">5</p>
  </div>
  <div class="rule" style="left:790px;width:376px;top:357px"></div>

  <div class="item col-right" style="top:366px">
    <h3 class="item-name">Beans &amp; Greens Quesadillas</h3>
    <p class="item-desc">greens, Mexican cheese, beans &amp; avocado, with<br>salsa</p>
    <p class="item-price">5</p>
  </div>
  <div class="rule" style="left:790px;width:376px;top:469px"></div>

  <div class="item col-right" style="top:478px">
    <h3 class="item-name">Sproutt Burrito</h3>
    <p class="item-desc">greens, Mexican cheese, beans, brown rice,<br>roasted chili corn &amp; avocado, with ancho chili<br>salsa, wheat tortilla</p>
    <p class="item-price">5</p>
  </div>

  <!-- Dessert -->
  <h2 class="section-title" style="left:911px;top:621px;width:132px;height:47px">DESSERT</h2>

  <div class="item col-right" style="top:692px">
    <h3 class="item-name">Strawberry Balsamic Ice Cream<br>Sundae</h3>
    <p class="item-price">5</p>
  </div>
  <div class="rule" style="left:790px;width:376px;top:773px"></div>

  <div class="item col-right" style="top:783px">
    <h3 class="item-name">Exotic Fruit Bowl</h3>
    <p class="item-price">5</p>
  </div>
  <div class="rule" style="left:790px;width:376px;top:842px"></div>

  <div class="item col-right" style="top:852px">
    <h3 class="item-name">White and Dark Oatmeal Cookie</h3>
    <p class="item-price">5</p>
  </div>
</main>
</body>
</html>
```